K & R Fabrications HVAC Mechanical Contractor Business Card

We need a business card for a HVAC/Plumbing Mechanical Contractor. Our website is http://www.krfabrications-demo.com. We would like to include the picture of the person on the card. Pictures of people for mock-ups can be found on our website. The blue on our logo is our primary color. We'd like this to be bold yet professional without too many colors but with some color to make sure it stands out.

Industry/Entity Type

Business

Contact Information for Business Card

Font styles to use
Sans Serif

Colors
000000

Requirements
Must have
• Our logo
• Person's picture
• Company Name
• Company Phone
• Person's email address
• Person's phone number
Nice to have
• Company Address
Should not have
• Clip art

```html
<!DOCTYPE html>
<html lang="en">
<head>
<meta charset="utf-8">
<title>K &amp; R Fabrications – Business Card</title>
<link href="https://fonts.googleapis.com/css2?family=Roboto+Condensed:wght@400;700&display=swap" rel="stylesheet">
<style>
  :root {
    --ink: #000000;
    --card: #050505;
    --brand-blue: #4a7cc4;
    --brand-blue-deep: #3d6ab0;
    --paper: #ffffff;
    --stage: #e9e6e1;
  }
  * { margin: 0; padding: 0; box-sizing: border-box; }
  html, body { width: 1200px; height: 901px; overflow: hidden; }
  body {
    background: var(--stage);
    font-family: "Roboto Condensed", Arial, sans-serif;
    position: relative;
  }
  .card {
    position: absolute;
    left: 380px; top: 65px;
    width: 440px; height: 770px;
    background: linear-gradient(160deg, #1a1a1a 0%, var(--card) 35%, var(--card) 100%);
    box-shadow: 0 10px 30px rgba(0,0,0,.25);
    overflow: hidden;
  }
  .company {
    position: absolute; left: 0; right: 0; top: 95px;
    text-align: center;
  }
  .company-name {
    color: var(--brand-blue);
    font-weight: 700;
    font-size: 40px;
    letter-spacing: .5px;
  }
  .company-tag {
    color: var(--paper);
    font-weight: 700;
    font-size: 18px;
    margin-top: 2px;
    padding-left: 90px;
  }
  .name-band {
    position: absolute; left: 0; right: 0; top: 228px; height: 104px;
    border-top: 8px solid var(--paper);
    border-bottom: 8px solid var(--paper);
    background: linear-gradient(90deg, var(--brand-blue-deep), var(--brand-blue));
    display: flex; flex-direction: column; justify-content: center;
    padding-left: 150px;
    color: var(--paper);
  }
  .person-name { font-weight: 700; font-size: 30px; line-height: 1; }
  .person-role { font-size: 20px; margin-top: 4px; }
  .brand-mark {
    position: absolute; left: 0; right: 0; top: 400px;
    display: flex; align-items: center; justify-content: center; gap: 12px;
  }
  .brand-mark .square { width: 26px; height: 26px; background: var(--brand-blue); }
  .brand-mark .brand-text { color: var(--paper); font-weight: 700; font-size: 26px; }
  .direct-line {
    position: absolute; right: 40px; top: 520px;
    color: var(--paper); font-size: 19px;
    display: flex; align-items: center; gap: 14px;
  }
  .contacts {
    position: absolute; left: 38px; top: 580px;
    list-style: none; color: var(--paper); font-size: 19px;
  }
  .contacts li { display: flex; align-items: center; gap: 12px; height: 34px; }
  .contacts svg, .direct-line svg { width: 16px; height: 16px; flex: none; }
</style>
</head>
<body>
  <article class="card">
    <header class="company">
      <div class="company-name">K &amp; R Fabrications, Inc.</div>
      <div class="company-tag">Mechanical Contractor</div>
    </header>

    <section class="name-band">
      <div class="person-name">Dale Mercer</div>
      <div class="person-role">Head of IT Services</div>
    </section>

    <div class="brand-mark">
      <span class="square"></span>
      <span class="brand-text">K &amp; R Fabrications</span>
    </div>

    <div class="direct-line">
      <svg viewBox="0 0 16 16"><path d="M3 1l3 3-2 2c1 2 3 4 5 5l2-2 3 3-2 3C7 15 1 9 0 4z" fill="#fff"/></svg>
      <span>555-273-0187</span>
    </div>

    <ul class="contacts">
      <li>
        <svg viewBox="0 0 16 16"><rect x="3" y="1" width="10" height="14" rx="2" fill="none" stroke="#fff" stroke-width="2"/></svg>
        <span>555-268-0142</span>
      </li>
      <li>
        <svg viewBox="0 0 16 16"><circle cx="8" cy="8" r="7" fill="none" stroke="#fff" stroke-width="1.6"/><path d="M1 8h14M8 1c-3 4-3 10 0 14M8 1c3 4 3 10 0 14" fill="none" stroke="#fff" stroke-width="1.2"/></svg>
        <span>www.krfabrications-demo.com</span>
      </li>
      <li>
        <svg viewBox="0 0 16 16"><rect x="1" y="3" width="14" height="10" fill="#fff"/><path d="M1 3l7 6 7-6" fill="none" stroke="#000" stroke-width="1.4"/></svg>
        <span>dmercer@krfabrications-demo.com</span>
      </li>
      <li>
        <svg viewBox="0 0 16 16"><path d="M8 0a5 5 0 0 1 5 5c0 4-5 11-5 11S3 9 3 5a5 5 0 0 1 5-5z" fill="#fff"/><circle cx="8" cy="5" r="2" fill="#000"/></svg>
        <span>1450 Ridgeline Avenue Fairview, WI 53700-0000</span>
      </li>
    </ul>
  </article>
</body>
</html>
```